Brisvane Partners Web Design

Dear all
I need a web design for a financial services site. We are a broker who deals with many different financial institutions and require a clean, simple and instantly impressive site based on the colour scheme that Mockwell created for us. A landing page (www.brisvn.mx) gives an idea of the logo and clour scheme but we are looking at either a one page site with rollover text boxes or a 3 or 4 page site depending on the preference of the designer and the best user experience. The site“s purpose is to give confidence that the company exists rather than impart pages of information although we would like this to be a site that can expand over time as the company grows. For now the requirement is for a clear set of possibly changing images at the centre of a white screen that relate to finance in general nad the benefits of wealth creation as well as sectios either along the top or bottom - Our Company, Our Approach, Our services, Our clients, Contact (user to fill in contact box to be sent to info@brisvn.mx. The text for each of these boxes I assume can be added by the coding team here, it the overall look and feel that I am looking for from Mockwell - deadline can be extended if necessary but I was hoping to wrap this all up in October

Target Market(s)

Succesful individuals looking to maximise returns on their investment via world class financial institutions and supported throughout by qualified independent financial advisors

Industry/Entity Type

Finance

Requirements
Must have
• Logo and color scheme of the logo design Mockwell sent - I have all these sourcefiles, pantone and fonts

```html
<!DOCTYPE html>
<html lang="en">
<head>
<meta charset="utf-8">
<title>Brisvane Partners</title>
<link href="https://fonts.googleapis.com/css2?family=Open+Sans:wght@300;400;600;700&display=swap" rel="stylesheet">
<style>
:root{
  --navy:#1b2a47;
  --gold:#f0a830;
  --white:#ffffff;
  --page:#fbfcfd;
  --body-text:#474b52;
  --icon:#7f8db0;
}
*{margin:0;padding:0;box-sizing:border-box}
html,body{width:1200px;height:1000px;overflow:hidden}
body{font-family:"Open Sans",Arial,sans-serif;background:var(--page);position:relative}
.top-rule{position:absolute;left:0;top:0;width:1200px;height:6px;background:var(--navy)}
.inquiry-tab{position:absolute;left:662px;top:0;width:418px;height:40px}
.inquiry-tab .tab-shape{position:absolute;left:0;top:0}
.phone-icon{position:absolute;left:34px;top:9px}
.inquiry-text{position:absolute;left:74px;top:10px;color:var(--white);font-size:16px;font-weight:400;white-space:nowrap}
.inquiry-text strong{color:var(--gold);font-weight:700}
.brand{position:absolute;left:132px;top:82px;display:flex;align-items:center;gap:10px}
.brand-mark{width:20px;height:20px;border-radius:50%;background:var(--navy)}
.brand-name{font-size:22px;font-weight:600;color:var(--navy);letter-spacing:.5px}
.main-nav{position:absolute;top:85px;left:442px;display:flex;gap:47px}
.main-nav a{font-size:19px;font-weight:600;color:var(--navy);text-decoration:none}
.hero{position:absolute;left:0;top:152px;width:1200px;height:641px;
  background:
    linear-gradient(180deg,rgba(0,0,0,0) 55%,rgba(20,20,25,.25) 100%),
    linear-gradient(90deg,#c9c3ae 0%,#9a7b58 14%,#6e5338 32%,#6a5236 50%,#5a4838 68%,#4e4236 84%,#5e5244 100%)}
.hero-copy{position:absolute;left:126px;top:152px;color:var(--white)}
.hero-title{font-size:49px;font-weight:300;line-height:58px;letter-spacing:-.2px}
.hero-sub{margin-top:32px;font-size:18px;font-weight:700}
.hero-actions{margin-top:38px;display:flex;align-items:center;gap:24px}
.btn-primary{display:block;width:194px;height:56px;border-radius:4px;background:linear-gradient(#4a5d82,#1d2c4b 60%,#16223c);box-shadow:0 2px 4px rgba(0,0,0,.35);color:var(--white);font-size:19px;font-weight:700;text-align:center;line-height:56px;text-decoration:none}
.link-more{color:var(--white);font-size:19px;font-weight:700;text-decoration:underline;text-underline-offset:3px}
.about{position:absolute;left:0;top:793px;width:1200px;height:207px;background:var(--page)}
.about-title{position:absolute;left:124px;top:38px;font-size:33px;font-weight:300;color:var(--navy)}
.about-image{position:absolute;left:126px;top:100px;width:387px;height:107px;background:linear-gradient(90deg,#f4f4f4,#e9e6e2 40%,#f6f6f6 70%,#ece8e2)}
.about-text{position:absolute;left:543px;top:94px;font-size:16.5px;line-height:25px;color:var(--body-text)}
.about-text span{display:block;white-space:nowrap}
</style>
</head>
<body>
<div class="top-rule"></div>
<div class="inquiry-tab">
  <svg class="tab-shape" width="418" height="40"><path d="M0 0H418L408 40H10Z" fill="#1b2a47"/></svg>
  <svg class="phone-icon" width="22" height="22" viewBox="0 0 22 22">
    <circle cx="11" cy="11" r="10" fill="none" stroke="#7f8db0" stroke-width="1.5"/>
    <path d="M7.5 6.5l2 0 1 2.5-1.3 1c.6 1.3 1.5 2.2 2.8 2.8l1-1.3 2.5 1v2c0 .6-.5 1-1.1 1C9.8 15.3 6.7 12.2 6.5 7.6c0-.6.4-1.1 1-1.1z" fill="#7f8db0"/>
  </svg>
  <div class="inquiry-text">FOR INQUIRIES, CALL US: <strong>(02) 5550 0147</strong></div>
</div>
<div class="brand"><span class="brand-mark"></span><span class="brand-name">Brisvane Partners</span></div>
<nav class="main-nav">
  <a href="#">About Us</a><a href="#">Our Approach</a><a href="#">Services</a><a href="#">Clients</a><a href="#">Contact Us</a>
</nav>
<section class="hero" role="img" aria-label="Hero photo: smiling businessman in a dark blazer against a warm blurred city background">
  <div class="hero-copy">
    <h1 class="hero-title">Designing investment<br>solutions for clients.</h1>
    <p class="hero-sub">Lorem ipsum dolor sit amet, consectetur adipisicing elit,</p>
    <div class="hero-actions"><a class="btn-primary" href="#">CONTACT US</a><a class="link-more" href="#">Learn More</a></div>
  </div>
</section>
<section class="about">
  <h2 class="about-title">About Brisvane Partners</h2>
  <div class="about-image" role="img" aria-label="Photo of two businesswomen talking in a bright office"></div>
  <p class="about-text">
    <span>Lorem ipsum dolor sit amet, consectetur adipisicing elit, sed do eius-</span>
    <span>mod tempor incididunt ut labore et dolore magna aliqua. Ut enim ad</span>
    <span>minim veniam, quis nostrud exercitation ullamco laboris nisi ut ali-</span>
    <span>quip ex ea commodo consequat.</span>
  </p>
</section>
</body>
</html>
```